Business Card Design

We Need a business card design for my company based in Tv Radio and music Productions and hunt Talent.

Industry/Entity Type

Business

Contact Information for Business Card

BrentaVue Production's, Teodor Vignoles,Cell Phone 318 4957310
Musician, Productor, Hunt Talent. Miami Fla. www.brentavue.net Mail. teodorvignoles@mailvana.com

```html
<!DOCTYPE html>
<html lang="en">
<head>
<meta charset="utf-8">
<title>BrentaVue Production's — Business Card</title>
<link href="https://fonts.googleapis.com/css2?family=Quicksand:wght@500;600&display=swap" rel="stylesheet">
<style>
  :root {
    --purple: #7b4aa0;
    --yellow: #fbd334;
    --ink: #1f1f1f;
    --white: #ffffff;
    --rule: #555555;
    --backdrop: #eeeae4;
  }
  * { margin: 0; padding: 0; box-sizing: border-box; }
  html, body { width: 1200px; height: 1000px; overflow: hidden; }
  body {
    position: relative;
    background: var(--backdrop);
    font-family: "Quicksand", sans-serif;
    color: var(--ink);
  }
  .card {
    position: absolute;
    width: 527px;
    height: 300px;
    background: var(--white);
    box-shadow: 0 2px 6px rgba(0,0,0,0.15);
  }
  /* Front */
  .card-front { left: 336px; top: 210px; }
  .front-frame {
    position: absolute;
    left: 11px; top: 10px; right: 10px; bottom: 10px;
    border: 12px solid var(--purple);
  }
  .front-inner {
    position: absolute;
    left: 9px; top: 9px; right: 9px; bottom: 9px;
    border: 6px solid var(--yellow);
  }
  .brand-mark {
    position: absolute;
    display: flex;
    align-items: center;
    gap: 10px;
    font-weight: 600;
    color: var(--ink);
    white-space: nowrap;
  }
  .brand-dot {
    border-radius: 50%;
    background: var(--yellow);
    flex: none;
  }
  .card-front .brand-mark {
    left: 50%; top: 50%;
    transform: translate(-50%, -50%);
    font-size: 38px;
  }
  .card-front .brand-dot { width: 44px; height: 44px; }

  /* Back */
  .card-back { left: 479px; top: 526px; }
  .band { position: absolute; left: 0; right: 0; }
  .band-yellow-top { top: 0; height: 14px; background: var(--yellow); }
  .band-purple-top { top: 18px; height: 7px; background: var(--purple); }
  .band-purple-bottom { bottom: 19px; height: 7px; background: var(--purple); }
  .band-yellow-bottom { bottom: 0; height: 14px; background: var(--yellow); }

  .card-back .brand-mark {
    left: 30px; top: 149px;
    transform: translateY(-50%);
    font-size: 20px;
    gap: 6px;
  }
  .card-back .brand-dot { width: 22px; height: 22px; }

  .details {
    position: absolute;
    left: 179px; top: 44px;
    width: 329px;
    text-align: center;
  }
  .company { font-size: 19px; font-weight: 500; line-height: 24px; letter-spacing: 0.3px; }
  .person { font-size: 19px; font-weight: 500; line-height: 28px; color: var(--purple); letter-spacing: 0.3px; }
  .rule { height: 1px; background: var(--rule); margin: 0; }
  .rule-top { margin-top: 16px; }
  .contact { list-style: none; padding: 13px 0 13px; }
  .contact li { font-size: 17px; font-weight: 500; line-height: 25px; }
  .roles {
    display: flex;
    justify-content: space-between;
    padding-top: 14px;
    font-size: 17px;
    font-weight: 500;
  }
  .roles .sep { color: var(--purple); }
</style>
</head>
<body>
  <section class="card card-front" aria-label="Business card front">
    <div class="front-frame"><div class="front-inner"></div></div>
    <div class="brand-mark"><span class="brand-dot"></span>BrentaVue</div>
  </section>

  <section class="card card-back" aria-label="Business card back">
    <div class="band band-yellow-top"></div>
    <div class="band band-purple-top"></div>

    <div class="brand-mark"><span class="brand-dot"></span>BrentaVue</div>

    <div class="details">
      <p class="company">BrentaVue Production's</p>
      <p class="person">Teodor Vignoles</p>
      <div class="rule rule-top"></div>
      <ul class="contact">
        <li>318 4957310</li>
        <li>www.brentavue.net</li>
        <li>teodorvignoles@mailvana.com</li>
      </ul>
      <div class="rule"></div>
      <p class="roles">
        <span>Musician</span><span class="sep">-</span><span>Productor</span><span class="sep">-</span><span>Hunt Talent</span>
      </p>
    </div>

    <div class="band band-purple-bottom"></div>
    <div class="band band-yellow-bottom"></div>
  </section>
</body>
</html>
```